Pantry Circle is an online food market place that connects foodies who make or grow great food with

We would like a 1/2 A4 page size flyer in landscape to promote our new business. We would like to encourage new home foodies to sign up for a membership on our website www.pantrycirclenz.co.nz and we would like customers who are looking for great food in their local community to search our website for their closest home foodie and support a neighbour who is growing or producing creative food locally

Target Market(s)

Creative food lovers

Industry/Entity Type

Landscape

Colors
acd037
f78f20
33b8a4

Requirements
Must have
• Food images and look groovy
• Must be easy to read and stand out on a notice board
• Website address www.pantrycirclenz.co.nz
Nice to have
• We wish to use this flyer in multiple locations and wish to put in different contact details prior to printing

```html
<!DOCTYPE html>
<html lang="en">
<head>
<meta charset="utf-8">
<title>Pantry Circle – Flyer</title>
<link rel="stylesheet" href="https://fonts.googleapis.com/css2?family=Arimo:wght@400;700&family=Roboto+Condensed:wght@700&display=swap">
<style>
  :root {
    --stage: #1c1c1c;
    --wood-light: #a89a88;
    --wood-mid: #8a7b69;
    --wood-dark: #6e604f;
    --brown: #4a2a14;
    --green: #3b8f3a;
    --kraft: #b89a68;
    --napkin: #5fc3c0;
    --napkin-deep: #2f9e9b;
    --utensil: #8a4a22;
    --panel: #f6f6f5;
    --ink: #222222;
    --white: #ffffff;
  }
  * { box-sizing: border-box; margin: 0; padding: 0; }
  html, body { width: 1200px; height: 999px; overflow: hidden; }
  body { background: var(--stage); position: relative; font-family: "Arimo", Arial, sans-serif; }

  .flyer {
    position: absolute; left: 60px; top: 118px; width: 1080px; height: 764px; overflow: hidden;
  }
  .wood-backdrop {
    position: absolute; inset: 0;
    background: linear-gradient(180deg, var(--wood-light) 0%, var(--wood-mid) 45%, var(--wood-light) 70%, var(--wood-dark) 100%);
  }
  .table-setting {
    position: absolute; left: 0; top: 30px; width: 440px; height: 734px;
    background: linear-gradient(160deg, var(--utensil) 0%, var(--napkin) 30%, var(--napkin-deep) 65%, var(--napkin) 100%);
    clip-path: polygon(0 0, 55% 0, 100% 72%, 100% 100%, 0 100%);
  }

  .brand { position: absolute; left: 252px; top: 34px; width: 176px; height: 176px; }
  .brand-disc { position: absolute; inset: 0; border-radius: 50%; background: var(--kraft); }
  .brand-name {
    position: absolute; inset: 0; display: flex; align-items: center; justify-content: center;
    text-align: center; font-family: "Roboto Condensed", "Arial Narrow", sans-serif; font-weight: 700;
    font-size: 36px; line-height: 1; color: var(--brown);
  }

  .headline { position: absolute; left: 450px; top: 26px; width: 616px; text-align: center; color: var(--brown); }
  .halo { text-shadow: -2px -2px 0 var(--white), 2px -2px 0 var(--white), -2px 2px 0 var(--white), 2px 2px 0 var(--white), 0 2px 0 var(--white), 0 -2px 0 var(--white); }
  .headline-intro { font-family: "Roboto Condensed", "Arial Narrow", sans-serif; font-weight: 700; font-size: 38px; line-height: 48px; }
  .headline-main { font-family: "Roboto Condensed", "Arial Narrow", sans-serif; font-weight: 700; font-size: 76px; line-height: 84px; color: var(--green); }
  .headline-sub { font-family: "Arimo", Arial, sans-serif; font-weight: 700; font-size: 39px; line-height: 50px; }

  .snapshot { position: absolute; background: var(--white); padding: 6px; box-shadow: 0 3px 8px rgba(0,0,0,.35); }
  .snapshot > div { width: 100%; height: 100%; }
  .snapshot-herbs { left: 438px; top: 292px; width: 218px; height: 238px; transform: rotate(-4deg); }
  .snapshot-herbs > div { background: linear-gradient(150deg, #3f6b35, #7ea46a 55%, #c9d6d8); }
  .snapshot-cook { left: 617px; top: 272px; width: 192px; height: 218px; }
  .snapshot-cook > div { background: linear-gradient(180deg, #e9e4df, #c7b8a8 55%, #b8553a); }
  .snapshot-tart { left: 778px; top: 302px; width: 204px; height: 218px; transform: rotate(4deg); }
  .snapshot-tart > div { background: linear-gradient(150deg, #d98a8e, #c23a3a 45%, #e0a64a 80%, #6a4a30); }

  .info-panel {
    position: absolute; left: 460px; top: 540px; width: 600px; height: 177px;
    background: var(--panel); border-radius: 12px; padding: 14px 22px;
    font-size: 19px; line-height: 25px; color: var(--ink);
  }
  .info-panel p + p { margin-top: 14px; }
  .contact {
    position: absolute; left: 460px; top: 724px; width: 600px; text-align: right; padding-right: 20px;
    font-size: 18px; color: var(--white); text-shadow: 0 1px 2px rgba(0,0,0,.5);
  }
  .contact strong { color: #111; text-shadow: 0 0 3px var(--white), 0 0 3px var(--white); }
</style>
</head>
<body>
  <main class="flyer">
    <div class="wood-backdrop" role="img" aria-label="Weathered grey-brown wooden table boards"></div>
    <div class="table-setting" role="img" aria-label="Turquoise gingham napkin with wooden salad spoons tied with raffia"></div>

    <div class="brand">
      <div class="brand-disc"></div>
      <div class="brand-name">Pantry<br>Circle</div>
    </div>

    <header class="headline">
      <p class="headline-intro halo">Be part of our exciting new online</p>
      <h1 class="headline-main halo">food marketplace</h1>
      <p class="headline-sub halo">connecting foodies in your<br>local community</p>
    </header>

    <figure class="snapshot snapshot-herbs"><div role="img" aria-label="Fresh garden herbs with scissors and twine"></div></figure>
    <figure class="snapshot snapshot-tart"><div role="img" aria-label="Fruit tart topped with berries"></div></figure>
    <figure class="snapshot snapshot-cook"><div role="img" aria-label="Home cook tossing a fresh salad in a kitchen"></div></figure>

    <section class="info-panel">
      <p>As a foodie you can sell your beautiful home produced or home grown produce on our marketplace website</p>
      <p>As a food lover you can purchase lovingly grown or prepared food and support your local foodie community while keeping your food miles low</p>
    </section>

    <p class="contact">For more information go to: <strong>www.pantrycirclenz.co.nz</strong></p>
  </main>
</body>
</html>
```